Veradine Contracting Folder

Creating a design for the cover of our folders that we pass to our customers

Want to keep the same look as our colors and fonts as attached

```html
<!DOCTYPE html>
<html lang="en">
<head>
<meta charset="utf-8">
<title>Veradine Contracting Folder</title>
<link href="https://fonts.googleapis.com/css2?family=Oswald:wght@500&family=Questrial&display=swap" rel="stylesheet">
<style>
  :root {
    --canvas: #e4e4e8;
    --navy: #1f1b78;
    --navy-deep: #1a176a;
    --band: #2a2a8c;
    --band-light: #33339a;
    --sky-top: #8f93c4;
    --sky-mid: #b7a9c9;
    --dusk: #d9a88c;
    --house: #6d7189;
    --street: #4a4f66;
    --lawn: #5f8a3a;
    --ink-light: #eef0ff;
    --logo: #1e1c7a;
  }
  * { margin: 0; padding: 0; box-sizing: border-box; }
  html, body { width: 1200px; height: 1200px; overflow: hidden; }
  body {
    background: var(--canvas);
    font-family: "Questrial", sans-serif;
    position: relative;
  }
  .panel {
    position: absolute;
    top: 100px;
    width: 520px;
    height: 1000px;
    overflow: hidden;
    box-shadow: 0 12px 30px rgba(0,0,0,0.18);
  }
  .front-cover { left: 60px; }
  .back-cover { left: 620px; background: var(--navy); }

  /* Front cover */
  .cover-photo {
    position: absolute;
    inset: 0 0 90px 0;
    background: linear-gradient(180deg,
      var(--sky-top) 0%,
      var(--sky-mid) 28%,
      var(--house) 52%,
      var(--house) 68%,
      var(--lawn) 76%,
      var(--street) 86%,
      #3d415a 100%);
  }
  .cover-shade {
    position: absolute;
    inset: 0;
    width: 100%;
    height: 100%;
  }
  .brand {
    position: absolute;
    top: 78px;
    left: 40px;
    color: var(--logo);
    font-family: "Oswald", sans-serif;
    font-weight: 500;
    display: flex;
    flex-direction: column;
    line-height: 1;
  }
  .brand-name {
    font-size: 76px;
    letter-spacing: 2px;
    text-transform: uppercase;
  }
  .brand-sub {
    font-size: 26px;
    letter-spacing: 7px;
    margin-top: 8px;
    margin-left: 14px;
  }
  .cover-band {
    position: absolute;
    left: 0; right: 0; bottom: 0;
    height: 90px;
    background: var(--band);
    color: var(--ink-light);
    font-size: 34px;
    display: flex;
    align-items: center;
    padding-left: 22px;
    letter-spacing: 0.3px;
  }

  /* Back cover */
  .back-art {
    position: absolute;
    inset: 0;
    width: 100%;
    height: 100%;
  }
  .back-intro {
    position: absolute;
    top: 44px;
    left: 24px;
    width: 380px;
    color: var(--ink-light);
    font-size: 14px;
    line-height: 1.75;
  }
  .back-contact {
    position: absolute;
    top: 690px;
    left: 44px;
    color: var(--ink-light);
    font-size: 14px;
    line-height: 1.8;
  }
  .back-contact .gap { margin-top: 10px; }
  .back-band {
    position: absolute;
    left: 0; right: 0; bottom: 0;
    height: 90px;
    background: var(--band-light);
    color: var(--ink-light);
    font-size: 28px;
    display: flex;
    align-items: center;
    justify-content: center;
    letter-spacing: 0.5px;
  }
</style>
</head>
<body>

  <section class="panel front-cover">
    <div class="cover-photo" role="img" aria-label="Photo of a two-storey suburban house with garage and wet driveway at dusk"></div>
    <svg class="cover-shade" viewBox="0 0 520 1000" preserveAspectRatio="none" aria-hidden="true">
      <polygon points="520,700 520,910 300,910" fill="var(--navy)" fill-opacity="0.75"/>
    </svg>
    <div class="brand">
      <span class="brand-name">Veradine</span>
      <span class="brand-sub">Contracting</span>
    </div>
    <div class="cover-band">Painting &amp; Contracting Consultancy</div>
  </section>

  <section class="panel back-cover">
    <svg class="back-art" viewBox="0 0 520 1000" preserveAspectRatio="none" aria-hidden="true">
      <defs>
        <linearGradient id="backPhoto" x1="0" y1="0" x2="0" y2="1">
          <stop offset="0" stop-color="#7f82b8"/>
          <stop offset="0.4" stop-color="#5e628f"/>
          <stop offset="0.65" stop-color="#4c507a"/>
          <stop offset="0.8" stop-color="#3f5a46"/>
          <stop offset="1" stop-color="#34385c"/>
        </linearGradient>
        <clipPath id="arcClip">
          <path d="M520,40 C330,90 170,280 90,560 L90,910 L520,910 Z"/>
        </clipPath>
      </defs>
      <rect width="520" height="1000" fill="var(--navy)"/>
      <rect x="0" y="0" width="520" height="910" fill="url(#backPhoto)" clip-path="url(#arcClip)" role="img" aria-label="Faded photo of the same house under a blue tint"/>
      <rect x="0" y="0" width="520" height="910" fill="var(--navy)" fill-opacity="0.45" clip-path="url(#arcClip)"/>
    </svg>
    <p class="back-intro">Lorem Ipsum is simply dummy text of the printing and typesetting industry. Lorem Ipsum has been the industry's standard dummy text ever since the 1500s, when an unknown printer took a galley of type and scrambled it to make a type specimen book. It has survived not only five centuries</p>
    <div class="back-contact">
      <p>Dummy city</p>
      <p>Dummy Country Land</p>
      <p class="gap">Tel. 1-555-208614</p>
      <p>Web: www.veradinebuild.com</p>
      <p>Email: hello@veradinebuild.com</p>
    </div>
    <div class="back-band">www.veradinebuild.com</div>
  </section>

</body>
</html>
```